We need a cover designed for our book on parenting. The focus of this book is on the parents, not on the child! We like the idea of this title having a double meaning - insight as in gaining insights into parenting, and "in sight" as in looking inward as parents and how to improve ourselves rather than looking outward to improve our children. We would love for the cover to somehow represent this double meaning. I can upload an excerpt from the book soon over the next few days.
Updates

Reason: We are still reviewing the amazing designs! Thank you so much! :)

Target Market(s)

Parents with kids of any age from babies through adult children.

Requirements
Must have
• Title is: Steady Hearth Homes
• Subtitle is: Building Calm Households Daily
• Authors names: Tara Bellwin, LCSW Dorian Bellwin, Ph.D.

```html
<!DOCTYPE html>
<html lang="en">
<head>
<meta charset="UTF-8">
<title>Steady Hearth Homes — Book Cover</title>
<link rel="stylesheet" href="https://fonts.googleapis.com/css2?family=Anton&family=Josefin+Sans:wght@400;600;700&display=swap">
<style>
  :root {
    --backdrop: #f2f2f2;
    --cover-mint: #93d5b8;
    --floor-mint: #a9dfc6;
    --frame-purple: #7a33d9;
    --title-yellow: #f4f132;
    --title-red: #ff5a5f;
    --title-purple: #7b34d6;
    --photo-top: #9bd8bd;
    --photo-mid: #5b6f86;
    --photo-low: #2f3b55;
  }
  * { box-sizing: border-box; margin: 0; padding: 0; }
  html, body {
    width: 1200px;
    height: 800px;
    overflow: hidden;
    background: var(--backdrop);
  }
  .canvas {
    width: 1200px;
    height: 800px;
    display: flex;
    align-items: center;
    justify-content: center;
  }
  .cover {
    position: relative;
    width: 480px;
    height: 720px;
    background: var(--cover-mint);
    overflow: hidden;
  }
  .cover-floor {
    position: absolute;
    left: 0; right: 0; bottom: 0;
    height: 110px;
    background: var(--floor-mint);
  }
  .cover-frame {
    position: absolute;
    inset: 0;
  }
  .title {
    position: absolute;
    left: 38px;
    top: 78px;
    width: 410px;
    font-weight: normal;
  }
  .title-main {
    display: block;
    font-family: "Anton", sans-serif;
    font-size: 66px;
    line-height: 1;
    letter-spacing: 0.5px;
    white-space: nowrap;
  }
  .title-main .soft { color: var(--title-yellow); }
  .title-main .strong { color: var(--title-red); }
  .title-sub {
    display: block;
    margin-top: 12px;
    padding-left: 70px;
    font-family: "Josefin Sans", sans-serif;
    font-weight: 400;
    font-size: 70px;
    line-height: 1;
    letter-spacing: 8px;
    color: var(--title-purple);
  }
  .title-sub .heavy { font-weight: 700; }
  .subtitle {
    position: absolute;
    left: 40px;
    top: 262px;
    width: 400px;
    font-family: "Josefin Sans", sans-serif;
    font-weight: 600;
    font-size: 20px;
    letter-spacing: 1px;
    color: var(--title-purple);
    text-align: right;
  }
  .authors {
    position: absolute;
    left: 40px;
    top: 540px;
    width: 190px;
    font-family: "Josefin Sans", sans-serif;
    font-weight: 600;
    font-size: 17px;
    line-height: 1.5;
    color: var(--title-purple);
    list-style: none;
  }
  .authors .credential { font-weight: 400; }
  .cover-photo {
    position: absolute;
    left: 255px;
    top: 400px;
    width: 165px;
    height: 300px;
    border-radius: 40px 40px 10px 10px;
    background: linear-gradient(180deg, var(--photo-top) 0%, var(--photo-mid) 35%, var(--photo-low) 80%, var(--floor-mint) 100%);
    opacity: 0.85;
  }
</style>
</head>
<body>
  <main class="canvas">
    <section class="cover">
      <div class="cover-floor"></div>
      <svg class="cover-frame" width="480" height="720" viewBox="0 0 480 720" aria-hidden="true">
        <line x1="22" y1="40" x2="446" y2="40" stroke="var(--frame-purple)" stroke-width="3"/>
        <line x1="22" y1="40" x2="22" y2="650" stroke="var(--frame-purple)" stroke-width="3"/>
      </svg>
      <h1 class="title">
        <span class="title-main"><span class="soft">Steady</span><span class="strong">HEARTH</span></span>
        <span class="title-sub">HO<span class="heavy">ME</span>S</span>
      </h1>
      <p class="subtitle">Building Calm Households Daily</p>
      <ul class="authors">
        <li>Tara Bellwin, <span class="credential">LCSW</span></li>
        <li>Dorian Bellwin, <span class="credential">Ph.D.</span></li>
      </ul>
      <div class="cover-photo" role="img" aria-label="Photograph of a mother walking and lifting her baby up high"></div>
    </section>
  </main>
</body>
</html>
```